Website Revamp to a Legal Tech Company

We are a Legal Technology Company and we are revamping our whole company from the logo (already done) to the website. We have built a custom portal and harnessed the use of AI and automation.

Current Website - https://www.velmarix.com/

We need a new website that looks like a tech company
Some examples of websites for samples
1. What we have today - https://www.velmarix.com/
2. https://pinwolegal.com/
3. https://www.brimfoxhub.com/
4. https://www.taru.com/
5.https://www.sotrimlaw.com/
6. https://www.murabex.com/

Hope this helps. Let's start with the Home page.
Once we agree on the basis design and the first 3-4 pages - we can handle the coding etc. Will have the content over once we have the basic homepage design.

Links that we will possibly have and want
1. Home
2. About Us
3. Place your Order
4. Free First File offer to all new customers
5. Services/Products
6. Transparent Pricing
7. Contact Us

Terms & Conditions and Privacy Policy will be added at the bottom of the page but our internal designers.

Hope this helps.

Target Market(s)

Personal Injury Law Firms in the US

Industry/Entity Type

Legal Tech Services

Coding

Coded - Design and coding required

Number of Pages Required

4 page

Colors

Designer to choose colors to be used in the design.

Requirements
Must have
• Need to look like a Tech company website
Nice to have
• The color Blue

```html
<!DOCTYPE html>
<html lang="en">
<head>
<meta charset="utf-8">
<title>Velmarix AI – Home</title>
<link href="https://fonts.googleapis.com/css2?family=Poppins:wght@400;500;600&family=Roboto:wght@400;500;700&display=swap" rel="stylesheet">
<style>
:root{
  --blue:#0d5092;
  --blue-dark:#083a70;
  --blue-deep:#06305e;
  --ink:#222831;
  --text:#4a4f57;
  --muted:#7b828c;
  --pale:#f1f6fc;
  --line:#d9e2ec;
  --grey:#6f6f72;
  --black:#111214;
  --white:#ffffff;
}
*{box-sizing:border-box;margin:0;padding:0}
html,body{width:1200px;height:4934px;overflow:hidden}
body{position:relative;font-family:'Roboto',sans-serif;color:var(--text);background:var(--white)}
.abs{position:absolute}
h1,h2,h3{font-family:'Poppins',sans-serif;font-weight:500;color:var(--ink)}
.section-title{position:absolute;left:0;width:1200px;text-align:center;font-size:38px}
.section-title::after{content:"";display:block;width:78px;height:4px;background:var(--blue);margin:6px auto 0}
.btn{position:absolute;display:flex;align-items:center;justify-content:center;border-radius:24px;font-size:14px;font-weight:500;text-transform:uppercase;letter-spacing:.2px}
.btn-blue{background:var(--blue);color:var(--white)}
.btn-white{background:var(--white);color:var(--ink)}
.btn-outline{border:1.5px solid var(--blue);color:var(--ink);background:var(--white)}
.photo{position:absolute}

/* hero */
.hero{position:absolute;left:0;top:0;width:1200px;height:620px;background:linear-gradient(120deg,#0b4a8c,#0d5092 55%,#0a427f);clip-path:polygon(0 0,100% 0,100% 548px,0 618px)}
.logo{position:absolute;display:flex;align-items:center;gap:10px;font-family:'Roboto',sans-serif;font-weight:700;font-size:24px;color:var(--white)}
.logo-mark{width:18px;height:18px;background:var(--white)}
.nav{position:absolute;left:316px;top:45px;display:flex;gap:28px;font-size:13px;color:var(--white)}
.nav .active{border-bottom:2px solid var(--white);padding-bottom:3px}
.contact-btn{position:absolute;left:1036px;top:38px;width:122px;height:36px;border:1.5px solid var(--white);border-radius:20px;color:var(--white);font-size:11px;font-weight:700;display:flex;align-items:center;justify-content:center}
.hero-title{position:absolute;left:110px;top:210px;font-size:40px;line-height:48px;color:var(--white);font-weight:500}
.hero-sub{position:absolute;left:110px;top:320px;font-size:18px;line-height:29px;color:var(--white)}
.hero-ring{position:absolute;left:625px;top:132px;width:464px;height:464px;border:3px solid var(--white);border-radius:50%}
.hero-photo{left:652px;top:159px;width:410px;height:410px;border-radius:50%;background:radial-gradient(circle at 55% 40%,#f3f5f8,#c9d3de 60%,#8a9db3)}
.follow{position:absolute;left:1148px;top:160px;writing-mode:vertical-rl;font-size:11px;font-weight:700;color:var(--white);letter-spacing:.5px}
.social-col{position:absolute;left:1140px;top:277px;display:flex;flex-direction:column;gap:12px}
.social-col span{width:30px;height:30px;border:1.5px solid var(--white);border-radius:50%}

/* intro */
.intro-text{position:absolute;left:120px;top:930px;width:960px;text-align:center;font-size:15.5px;line-height:27.5px}
.tabs{position:absolute;left:0;top:1218px;width:1200px;display:flex;justify-content:center;gap:8px}
.tab{height:50px;padding:0 28px;border:1.5px solid var(--blue);border-radius:26px;display:flex;align-items:center;font-size:14px;font-weight:500;color:var(--ink)}
.tab.on{background:var(--blue);color:var(--white)}
.frame{position:absolute;border:2px solid var(--blue);border-radius:26px}
.case-title{position:absolute;left:617px;top:1350px;font-size:36px}
.case-title::after,.svc-title::after{content:"";display:block;width:76px;height:4px;background:var(--blue);margin-top:6px}
.case-text{position:absolute;left:617px;top:1440px;width:472px;font-size:14.5px;line-height:25.5px;text-align:justify}
.case-text p+p{margin-top:12px}

/* services */
.svc-bg{position:absolute;left:0;top:1800px;width:1200px;height:1320px;background:var(--pale);clip-path:polygon(0 180px,560px 60px,1200px 160px,1200px 100%,0 100%)}
.svc-tab{position:absolute;top:2055px;width:464px;height:102px;display:flex;align-items:center;gap:32px;padding-left:10px;background:var(--white);box-shadow:0 4px 14px rgba(13,80,146,.12);font-size:15.5px;font-weight:500;line-height:27px;color:var(--ink);text-transform:uppercase}
.svc-tab .ico{width:84px;height:84px;background:var(--blue);display:flex;align-items:center;justify-content:center}
.svc-tab.on{background:var(--blue);color:var(--white);border:3px solid #c9dcf0}
.svc-tab.on .ico{background:var(--white)}
.svc-title{position:absolute;left:111px;top:2238px;width:460px;font-size:32px;line-height:40px}
.svc-text{position:absolute;left:111px;top:2384px;width:470px;font-size:14.5px;line-height:25.5px;text-align:justify}
.svc-text p+p{margin-top:12px}
.features{position:absolute;left:111px;top:2730px;display:flex;gap:22px}
.feature{width:228px;height:293px;background:var(--white);box-shadow:0 4px 14px rgba(0,0,0,.07);text-align:center;padding:30px 20px 0}
.feature.on{border:3px solid var(--blue)}
.feature .circ{width:90px;height:90px;border-radius:50%;background:#dce8f4;margin:0 auto 26px;display:flex;align-items:center;justify-content:center}
.feature.on .circ{background:var(--blue)}
.feature h3{font-family:'Roboto',sans-serif;font-size:14.5px;font-weight:500;line-height:25px;color:var(--ink);text-transform:uppercase}
.feature p{font-size:13.5px;line-height:22px;margin-top:6px}

/* blog */
.blog-band{position:absolute;left:0;top:3121px;width:1200px;height:384px;background:var(--grey)}
.blog-title{color:var(--white)}
.blog-title::after{background:var(--white)}
.arrow{position:absolute;top:3377px;width:38px;height:38px;border-radius:50%;border:1.5px solid var(--white);display:flex;align-items:center;justify-content:center}
.arrow.r{background:var(--white)}
.blog-card{position:absolute;top:3280px;width:305px;height:481px;background:var(--white);border-radius:16px;box-shadow:0 6px 18px rgba(0,0,0,.12);padding:8px 8px 0;text-align:center}
.blog-card .img{height:222px;border-radius:12px}
.blog-card h3{font-family:'Roboto',sans-serif;font-size:15.5px;font-weight:500;line-height:25.5px;color:var(--ink);text-transform:uppercase;margin:22px 14px 0}
.blog-card p{font-size:13px;line-height:22px;margin:10px 18px 0}
.blog-card .btn{position:relative;width:130px;height:42px;margin:20px auto 0}

/* contact */
.contact-blue{position:absolute;left:109px;top:3869px;width:447px;height:387px;background:var(--blue)}
.contact-label{position:absolute;left:310px;top:3972px;font-size:19px;color:var(--white);font-weight:500}
.contact-head{position:absolute;left:200px;top:4024px;width:220px;text-align:right;font-family:'Poppins',sans-serif;font-weight:600;font-size:35px;line-height:53px;color:var(--white)}
.dots{position:absolute;background-image:radial-gradient(circle,#9aa3ad 1.3px,transparent 1.6px);background-size:12px 12px}
.outline-box{position:absolute;left:742px;top:3892px;width:366px;height:120px;border:3px solid #d3d5d8;border-bottom:none}
.form{position:absolute;left:460px;top:3920px;width:627px;height:435px;background:var(--white);box-shadow:0 6px 22px rgba(0,0,0,.12)}
.form h2{position:absolute;left:54px;top:44px;font-size:21px}
.field{position:absolute;width:228px;border-bottom:1px solid var(--line);padding-bottom:10px}
.field label{display:block;font-size:14px;font-weight:500;color:var(--ink)}
.field span{display:block;font-size:11px;color:var(--muted);margin-top:10px}
.send{position:absolute;left:502px;top:316px;width:64px;height:64px;border-radius:50%;background:var(--blue);display:flex;align-items:center;justify-content:center}

/* footer */
.footer{position:absolute;left:0;top:4430px;width:1200px;height:504px;background:var(--black);clip-path:polygon(0 156px,720px 0,1200px 120px,1200px 100%,0 100%)}
.footer-shade{position:absolute;left:980px;top:4470px;width:220px;height:120px;background:#dcdcdc;clip-path:polygon(0 100%,100% 0,100% 60%,30% 100%)}
.f-col h4{font-family:'Roboto',sans-serif;font-size:16px;font-weight:500;color:var(--white);text-transform:uppercase;margin-bottom:18px}
.f-nav li{list-style:none;color:var(--white);font-size:14px;line-height:33px;display:flex;align-items:center;gap:18px}
.f-nav li::before{content:"";width:9px;height:9px;border:2px solid var(--blue);border-radius:50%}
.f-nav .more{text-decoration:underline;font-weight:700;padding-left:29px}
.f-nav .more::before{display:none}
.f-item{display:flex;gap:22px;align-items:flex-start;color:var(--white);font-size:14px;line-height:22px;margin-bottom:14px}
.f-ico{flex:none;width:34px;height:34px;border-radius:50%;background:var(--white);display:flex;align-items:center;justify-content:center}
.f-line{position:absolute;left:111px;top:4882px;width:978px;height:1px;background:#3a3c40}
.copy{position:absolute;left:0;top:4896px;width:1200px;text-align:center;font-size:13px;color:var(--white)}
.copy a{color:var(--white)}
.f-social{position:absolute;left:898px;top:4893px;display:flex;gap:8px}
.f-social span{width:30px;height:30px;border:1.5px solid var(--white);border-radius:50%}
.f-social span.on{background:var(--blue);border-color:var(--blue)}
</style>
</head>
<body>

<!-- Hero -->
<section class="hero" aria-label="Hero">
  <div class="logo" style="left:111px;top:42px"><span class="logo-mark"></span>Velmarix AI</div>
  <nav class="nav">
    <span class="active">Home</span><span>About Us</span><span>Place your Order</span><span>Services</span><span>Pricing</span><span>Free First File offer to all new customers</span>
  </nav>
  <div class="contact-btn">CONTACT US</div>
  <h1 class="hero-title">Experience Offshore<br>Advantage</h1>
  <p class="hero-sub">Skilled Medical Experts. Substantial cost reduction.<br>Quick Turnaround. High Accuracy.</p>
  <div class="btn btn-white" style="left:110px;top:400px;width:150px;height:46px">Learn More</div>
  <div class="hero-ring"></div>
  <div class="photo hero-photo" role="img" aria-label="Smiling doctor in a white coat holding a tablet in a clinic"></div>
  <div class="follow">FOLLOW US ON</div>
  <div class="social-col" aria-label="Social links"><span></span><span></span><span></span><span></span><span></span></div>
</section>

<!-- Intro -->
<h2 class="section-title" style="top:845px">Organized Medical Docz</h2>
<p class="intro-text">Velmarix employs a team with expertise in retrieving, assembling, reviewing, and summarizing medical records and bills. We support law firms by handling all medical records-related tasks, thereby allowing attorneys to focus on other very important case-related matters, such as proving liability, causation, and damages. Velmarix is equipped to immediately handle any size project for a small, mid-sized, or large law firm. Our team works within a secure facility and adheres to the highest level of security and confidentiality in order to safeguard your client's records and privacy.</p>

<h2 class="section-title" style="top:1122px">Cases We Support</h2>
<div class="tabs">
  <div class="tab on">PERSONAL INJURY</div>
  <div class="tab">MASS TORT</div>
  <div class="tab">MEDICAL MALPRACTICE CASES</div>
</div>

<div class="frame" style="left:111px;top:1326px;width:441px;height:394px;border-right:none;border-bottom:none"></div>
<div class="photo" style="left:138px;top:1353px;width:437px;height:391px;border-radius:24px;background:linear-gradient(135deg,#e9eef3,#b8c8d8 55%,#5a7894)" role="img" aria-label="Hand holding a magnifying glass over a medical record checklist"></div>
<h2 class="case-title">Personal Injury</h2>
<div class="case-text">
  <p>With high volumes of medical records to be reviewed, lawyers handling personal injury cases need to clearly understand the nature of the injury and medical treatment, the extent of the harm and damages, and estimates of the future costs.</p>
  <p>The attorneys need to invest a significant amount of time in retrieving and reviewing the records, drafting a case summaries, drafting demand letters, preparing for litigation, and more.</p>
</div>
<div class="btn btn-blue" style="left:617px;top:1665px;width:140px;height:46px">Learn More</div>

<!-- Services -->
<svg class="abs" style="left:760px;top:1700px" width="440" height="240" aria-hidden="true"><polygon points="150,240 330,60 440,120 440,200 310,130 210,240" fill="#e3e3e3"/></svg>
<div class="svc-bg"></div>
<h2 class="section-title" style="top:1948px">Our Services</h2>

<div class="svc-tab" style="left:111px">
  <div class="ico"><svg width="34" height="40" viewBox="0 0 34 40"><circle cx="17" cy="9" r="7" fill="#fff"/><path d="M4 38v-9a9 9 0 0 1 9-9h8a9 9 0 0 1 9 9v9z" fill="#fff"/></svg></div>
  <span>Personal Injury Medical Records<br>Summaries and Reports</span>
</div>
<div class="svc-tab on" style="left:604px">
  <div class="ico"><svg width="40" height="38" viewBox="0 0 40 38"><rect x="3" y="3" width="34" height="24" rx="2" fill="none" stroke="#0d5092" stroke-width="3"/><rect x="14" y="8" width="12" height="14" fill="#0d5092"/><path d="M12 35h16M20 27v8" stroke="#0d5092" stroke-width="3"/></svg></div>
  <span>Retrieval, Assembly and<br>Organization of Medical Records</span>
</div>

<h2 class="svc-title">Retrieval, Assembly and Organization of Medical Records</h2>
<div class="svc-text">
  <p>Velmarix's team includes seasoned professionals with in-depth clinical knowledge so that you get unparalleled medico-legal services with a high degree of accuracy and reliability.</p>
  <p>We understand that one of the least productive tasks for your paralegals and attorneys is to review and translate the massive pile of medical data into digestible information to substantiate your claims.</p>
</div>
<div class="btn btn-blue" style="left:111px;top:2606px;width:154px;height:46px">Learn More</div>
<div class="frame" style="left:652px;top:2268px;width:436px;height:392px;border-left:none;border-top:none"></div>
<div class="photo" style="left:627px;top:2239px;width:436px;height:395px;border-radius:24px;background:linear-gradient(150deg,#dfe7ef,#aebfd0 50%,#7b94ad)" role="img" aria-label="Nurse writing on a clipboard beside a patient in a hospital bed"></div>

<div class="features">
  <div class="feature">
    <div class="circ"><svg width="40" height="40" viewBox="0 0 40 40"><rect x="8" y="6" width="24" height="28" rx="2" fill="#0d5092"/><path d="M20 14v12M14 20h12" stroke="#fff" stroke-width="3"/></svg></div>
    <h3>Medical Records Solution</h3>
    <p>We provide medical records solutions to small, mid-sized, or large law firms</p>
  </div>
  <div class="feature">
    <div class="circ"><svg width="40" height="40" viewBox="0 0 40 40"><circle cx="20" cy="20" r="13" fill="none" stroke="#0d5092" stroke-width="4" stroke-dasharray="6 3"/><circle cx="20" cy="20" r="5" fill="#0d5092"/></svg></div>
    <h3>Highly Trained Staff</h3>
    <p>Our staff has expertise in and received training on retrieving, reviewing, and summarizing medical records.</p>
  </div>
  <div class="feature on">
    <div class="circ"><svg width="40" height="40" viewBox="0 0 40 40"><path d="M20 6l4 9 10 1-8 7 3 10-9-6-9 6 3-10-8-7 10-1z" fill="#fff"/></svg></div>
    <h3>Highest Quality</h3>
    <p>We provide the highest quality medical records support services that will save your firm money, time, and effort.</p>
  </div>
  <div class="feature">
    <div class="circ"><svg width="40" height="40" viewBox="0 0 40 40"><rect x="9" y="6" width="20" height="27" rx="2" fill="#0d5092"/><circle cx="28" cy="28" r="8" fill="#fff" stroke="#0d5092" stroke-width="2"/><path d="M24 28l3 3 5-6" fill="none" stroke="#0d5092" stroke-width="2.5"/></svg></div>
    <h3>HIPAA and HITECH</h3>
    <p>We are HIPAA and HITECH compliant, and our staff follows strict rules-based security protocols.</p>
  </div>
</div>

<!-- Blog -->
<div class="blog-band"></div>
<h2 class="section-title blog-title" style="top:3184px">Latest Blog Post</h2>
<div class="arrow" style="left:37px"><svg width="14" height="14" viewBox="0 0 14 14"><path d="M9 2L4 7l5 5" fill="none" stroke="#fff" stroke-width="2"/></svg></div>
<div class="arrow r" style="left:1124px"><svg width="14" height="14" viewBox="0 0 14 14"><path d="M5 2l5 5-5 5" fill="none" stroke="#222" stroke-width="2"/></svg></div>

<article class="blog-card" style="left:111px">
  <div class="img" role="img" aria-label="Hand signing a medical document with a pen" style="background:linear-gradient(135deg,#eef2f6,#b9c7d6)"></div>
  <h3>Intentional Misuse of Social Media App May Lead to Developer Liability</h3>
  <p>Social media and messaging applications have changed the way people communicate.</p>
  <div class="btn btn-outline">Read More</div>
</article>
<article class="blog-card" style="left:449px">
  <div class="img" role="img" aria-label="Doctor reviewing electronic health records on a computer" style="background:linear-gradient(135deg,#e2e8ee,#9fb3c6)"></div>
  <h3>EHR &amp; EMR – How to Use Them Effectively in a Med Mal Case</h3>
  <p>Electronic Health Records (EHR) and Electronic Medical Records (EMR) provide a wealth of...</p>
  <div class="btn btn-blue">Read More</div>
</article>
<article class="blog-card" style="left:784px">
  <div class="img" role="img" aria-label="Doctor holding a tablet with glowing digital health icons" style="background:linear-gradient(135deg,#bcd8ea,#3c7fae)"></div>
  <h3>Is It Time to Remove the Word “Independent” From “IME”?</h3>
  <p>Plaintiff's bar has generally recognized that IMEs may be many things, but “independent” was clearly not one of them.</p>
  <div class="btn btn-outline">Read More</div>
</article>

<!-- Contact -->
<div class="outline-box"></div>
<div class="contact-blue"></div>
<div class="dots" style="left:74px;top:4160px;width:14px;height:150px"></div>
<div class="dots" style="left:74px;top:4296px;width:150px;height:14px"></div>
<div class="contact-label">Contact Us</div>
<div class="contact-head">LET'S DO GOOD TOGETHER!</div>
<form class="form">
  <h2>Send Us A Message</h2>
  <div class="field" style="left:58px;top:118px"><label>First Name</label><span>Alex</span></div>
  <div class="field" style="left:334px;top:118px"><label>Last Name</label><span>Morgan</span></div>
  <div class="field" style="left:58px;top:212px"><label>Email Address</label><span>alexmorgan@example.com</span></div>
  <div class="field" style="left:334px;top:212px"><label>Phone</label><span>+1 (888) 888 8888</span></div>
  <div class="field" style="left:58px;top:304px;width:450px"><label>Message</label><span>Lorem ipsum dolor sit a tetur adipiscing...|</span></div>
  <div class="send"><svg width="22" height="22" viewBox="0 0 22 22"><path d="M20 2L2 10l7 3 3 7z" fill="#fff"/></svg></div>
</form>

<!-- Footer -->
<div class="footer-shade"></div>
<footer class="footer"></footer>
<div class="logo" style="left:111px;top:4750px;font-size:30px"><span class="logo-mark" style="width:22px;height:22px"></span>Velmarix AI</div>

<div class="f-col abs" style="left:357px;top:4630px">
  <h4>Navigation</h4>
  <ul class="f-nav"><li>Home</li><li>About Us</li><li>Place your Order</li><li>Services</li><li>Pricing</li><li class="more">MORE</li></ul>
</div>
<div class="f-col abs" style="left:566px;top:4630px">
  <h4>Business Inquiries</h4>
  <div class="f-item"><span class="f-ico"><svg width="14" height="16" viewBox="0 0 14 16"><path d="M7 0a6 6 0 0 1 6 6c0 4-6 10-6 10S1 10 1 6a6 6 0 0 1 6-6z" fill="#0d5092"/><circle cx="7" cy="6" r="2" fill="#fff"/></svg></span><span>1820 Harbor Lane, Suite 4B<br>Coral Bay, FL 33199</span></div>
  <div class="f-item"><span class="f-ico"><svg width="16" height="12" viewBox="0 0 16 12"><rect width="16" height="12" rx="1" fill="#0d5092"/><path d="M1 1l7 6 7-6" fill="none" stroke="#fff" stroke-width="1.4"/></svg></span><span style="padding-top:6px">info@velmarix.com</span></div>
  <div class="f-item"><span class="f-ico"><svg width="14" height="14" viewBox="0 0 14 14"><path d="M3 0l3 3-2 2a8 8 0 0 0 5 5l2-2 3 3-2 3C6 14 0 8 0 2z" fill="#0d5092"/></svg></span><span style="padding-top:6px">(555) 014-2280</span></div>
</div>
<div class="f-col abs" style="left:849px;top:4630px">
  <h4>Records Processing</h4>
  <div class="f-item"><span class="f-ico"><svg width="14" height="16" viewBox="0 0 14 16"><path d="M7 0a6 6 0 0 1 6 6c0 4-6 10-6 10S1 10 1 6a6 6 0 0 1 6-6z" fill="#0d5092"/><circle cx="7" cy="6" r="2" fill="#fff"/></svg></span><span>42 Millbrook Road<br>Fairhollow, New York 11990</span></div>
  <div class="f-item"><span class="f-ico"><svg width="16" height="12" viewBox="0 0 16 12"><rect width="16" height="12" rx="1" fill="#0d5092"/><path d="M1 1l7 6 7-6" fill="none" stroke="#fff" stroke-width="1.4"/></svg></span><span style="padding-top:6px">records@velmarix.com</span></div>
  <div class="f-item"><span class="f-ico"><svg width="14" height="14" viewBox="0 0 14 14"><path d="M3 0l3 3-2 2a8 8 0 0 0 5 5l2-2 3 3-2 3C6 14 0 8 0 2z" fill="#0d5092"/></svg></span><span style="padding-top:6px">(555) 014-2280</span></div>
  <div class="f-item"><span class="f-ico"><svg width="14" height="14" viewBox="0 0 14 14"><rect x="1" y="4" width="12" height="9" fill="#0d5092"/><rect x="4" y="0" width="6" height="5" fill="#0d5092"/></svg></span><span style="padding-top:6px">(555) 014-7731</span></div>
</div>

<div class="f-line"></div>
<p class="copy">© 2024 Velmarix AI &nbsp;| &nbsp;<a href="#">Terms &amp; Conditions</a> &nbsp;| &nbsp;<a href="#">Privacy Policy</a></p>
<div class="f-social" aria-label="Social links"><span></span><span class="on"></span><span></span><span></span><span></span></div>

</body>
</html>
```